Web Design Project - (DESIGN AND FOLLOW UP CODING)

Web design for new management consultancy company

**About The Halvern Group

We work with organisations find and implement creative and sensible solutions...

We explore and inform…We have in-house research capability and enrich discussion through our own research, analysis and inputs. We interview staff and stakeholders, analyse data and literature and help you develop knowledge and solutions, and the plans to implement these.

We present new ideas…We develop proposals and reports that use internally and externally derived evidence to propose effective new solutions.

Specialties
Higher Education, TAFE, Local Government, Regional Development

Industry
Education Management
Updates

Target Market(s)

Business and government managers

Industry/Entity Type

Education

Requirements
Must have
• Sections:

**About
We work with organisations find and implement solutions to opportunities and challenges.
We explore and inform…
We present new ideas…

We develop proposals and reports that link internally and externally derived evidence to develop and implement new solutions.

Our three practice pillars are-
Ideas and partnerships:
Knowledgeable leaders:
Solutions:

** People
Martin Colbey (PHOTO) Bio

** Services
Acumen - Solutions - Partnerships -Implementation
- On time and within budget.
- Project leadership.
- Researched inputs and facilitated outcomes.
- Focus on implementation.
- Develop value-adding partnerships and get them funded
- Creative responses to funding opportunities
- Organisational reviews

Sectors
-Education
-State Government
- Local Government
- Utilities
- Financial services
- Health and ageing
- Human services
- Government
-Regional

** Careers

** Key Partners
With weblinks

** Contact

Links to Twitter LinkedIn Facebook
Nice to have
• Logo available from: quillmark@zevonet.com.au

```html
<!DOCTYPE html>
<html lang="en">
<head>
<meta charset="utf-8">
<title>The Halvern Group — Management Consultancy</title>
<link rel="stylesheet" href="https://fonts.googleapis.com/css2?family=Oswald:wght@400;500;600&family=Arimo:wght@400;700&family=Cinzel:wght@400;600&display=swap">
<style>
:root{
  --blue:#0a6699;
  --blue-dark:#0b5a86;
  --orange:#f0673a;
  --ink:#1b1b1b;
  --grey-bg:#f3f2f2;
  --hero-bg:#17161b;
  --rule:#c9c9c9;
  --text:#333;
}
*{margin:0;padding:0;box-sizing:border-box}
html,body{width:692px;height:1200px;overflow:hidden;background:var(--grey-bg)}
body{position:relative;font-family:"Arimo",Arial,sans-serif;color:var(--ink)}
.abs{position:absolute}

/* header */
.site-header{position:absolute;left:0;top:0;width:692px;height:95px;background:#fff}
.brand{position:absolute;left:43px;top:43px;font-family:"Oswald",sans-serif;font-weight:500;font-size:15px;color:var(--ink);letter-spacing:.6px;white-space:nowrap}
.main-nav a{position:absolute;top:44px;font-family:"Oswald",sans-serif;font-weight:500;font-size:13px;color:var(--blue);text-decoration:none;white-space:nowrap}
.main-nav .current{left:243px;top:0;width:76px;height:98px;background:var(--blue);color:#fff;font-size:15px;text-align:center;padding-top:42px;border-bottom:4px solid var(--blue-dark)}

/* hero */
.hero{position:absolute;left:0;top:95px;width:692px;height:218px;background:var(--hero-bg)}
.hero-photo{position:absolute;left:533px;top:0;width:136px;height:218px;background:linear-gradient(160deg,#3a3a3e,#c9c9c9 55%,#8d8d90)}
.hero-bar{position:absolute;left:669px;top:21px;width:23px;height:197px;background:var(--blue)}
.hero-f{position:absolute;left:136px;top:16px;font-family:"Oswald",sans-serif;font-weight:600;font-size:88px;line-height:72px;color:#fff}
.hero-line{position:absolute;font-family:"Oswald",sans-serif;font-weight:500;color:#fff;white-space:nowrap;line-height:1}
.hero-badge{position:absolute;left:176px;top:116px;width:158px;height:18px;background:var(--orange);color:#fff;font-size:8px;line-height:18px;text-align:center}

/* section title */
.section-title{position:absolute;font-family:"Oswald",sans-serif;font-weight:600;text-align:center;line-height:1}
.rule{position:absolute;height:1px;background:var(--rule)}

/* intro */
.intro-frame{position:absolute;left:107px;top:422px;width:86px;height:111px}
.intro-heading{position:absolute;left:199px;top:421px;font-family:"Cinzel",serif;font-size:10px;color:var(--orange)}
.intro-text{position:absolute;left:201px;top:455px;width:392px;font-size:7.3px;line-height:9.2px;color:#555}
.read-more{position:absolute;left:541px;top:528px;font-family:"Cinzel",serif;font-size:6px;color:var(--blue);text-decoration:none}

/* columns */
.col-title{position:absolute;font-weight:700;font-size:13.5px;white-space:nowrap}
.col-text{position:absolute;width:164px;font-size:10.5px;line-height:12.3px;color:#222}
.social-bar{position:absolute;left:45px;top:618px;width:155px;height:42px;background:#dedede;display:flex;align-items:center}
.social-mail{width:32px;height:42px;background:var(--blue);display:flex;align-items:center;justify-content:center}
.social-links{display:flex;gap:14px;padding-left:14px;align-items:center}
.reasons{position:absolute;left:236px;top:568px;width:207px;height:38px;background:var(--orange);color:#fff;display:flex;align-items:center;padding-left:37px;gap:12px;font-weight:700;font-size:7.5px}
.reasons b{font-size:16px}
.reasons-art{position:absolute;left:236px;top:611px;width:207px;height:144px;background:radial-gradient(circle at 50% 60%,#3fae45 0 35%,#2b8fa6 55%,#55c9e0 100%)}
.dotted{position:absolute;left:496px;top:674px;width:160px;border-top:1px dotted #bbb}

/* people */
.people-tab{position:absolute;left:68px;top:959px;width:60px;height:41px;background:var(--orange);border-radius:6px 0 0 6px}
.people-pill{position:absolute;left:110px;top:959px;width:310px;height:41px;background:#e2e1e1;border-radius:0 8px 8px 0}
.people-photo{position:absolute;left:101px;top:920px;width:108px;height:108px;border-radius:50%;border:3px solid #b9b9b9;background:radial-gradient(circle at 50% 40%,#d8c6b8,#8b8e96 70%,#2d3440)}
.people-name{position:absolute;left:228px;top:970px;font-weight:700;font-size:14px;color:var(--blue)}
.people-bio{position:absolute;font-size:9.6px;line-height:10.6px;color:#222}
.client{position:absolute;left:460px;width:180px;height:42px}
.client-photo{position:absolute;left:0;top:0;width:40px;height:40px;border-radius:50%;border:2px solid #ccc;background:radial-gradient(circle,#cdbdaf,#6d6a6a)}
.client-quote{position:absolute;left:49px;top:16px;font-size:8.3px;color:#222;white-space:nowrap}
.client-name{position:absolute;left:126px;top:29px;font-size:8.3px;color:var(--blue)}

/* footer */
.site-footer{position:absolute;left:0;top:1153px;width:692px;height:47px;background:var(--blue);color:#fff}
.foot-nav a{position:absolute;top:10px;font-size:8.2px;color:#fff;text-decoration:none}
.foot-sep{position:absolute;top:0;width:1px;height:27px;background:#fff;opacity:.8}
.copyright{position:absolute;left:0;top:34px;width:692px;text-align:center;font-size:6px}
</style>
</head>
<body>

<header class="site-header">
  <div class="brand">THE HALVERN GROUP</div>
  <nav class="main-nav">
    <a class="current" href="#">HOME</a>
    <a href="#" style="left:340px">ABOUT</a>
    <a href="#" style="left:404px">SERVICES</a>
    <a href="#" style="left:482px">SECTORS</a>
    <a href="#" style="left:558px">CAREERS</a>
    <a href="#" style="left:618px">CONTACT US</a>
  </nav>
</header>

<section class="hero">
  <div class="hero-f">F</div>
  <div class="hero-line" style="left:182px;top:22px;font-size:21px">IND THE SOLUTION</div>
  <div class="hero-line" style="left:275px;top:48px;font-size:10.5px">SOLVE YOUR</div>
  <svg class="abs" style="left:241px;top:50px" width="32" height="28" viewBox="0 0 32 28" aria-hidden="true">
    <g fill="none" stroke="var(--orange)" stroke-width="4" stroke-linecap="round">
      <rect x="14" y="2" width="14" height="9" rx="4.5" transform="rotate(-35 21 6.5)"/>
      <rect x="3" y="15" width="14" height="9" rx="4.5" transform="rotate(-35 10 19.5)"/>
    </g>
  </svg>
  <div class="hero-line" style="left:195px;top:80px;font-size:9.5px">COMPLICATED</div>
  <div class="hero-line" style="left:177px;top:90px;font-size:21px">PROBLEM</div>
  <div class="hero-badge">Management consultancy company</div>
  <div class="hero-photo" role="img" aria-label="Portrait of a consultant in suit and sunglasses"></div>
  <div class="hero-bar"></div>
</section>

<div class="rule" style="left:221px;top:344px;width:86px;background:#333"></div>
<div class="rule" style="left:333px;top:344px;width:93px;background:#333"></div>
<svg class="abs" style="left:317px;top:332px" width="12" height="22" viewBox="0 0 12 22" aria-hidden="true">
  <path d="M6 1C2 4 1 9 4 12c2 2 2 6 0 9 5-3 7-8 6-12C9 6 7 4 6 1z" fill="var(--orange)"/>
</svg>
<h2 class="section-title" style="left:221px;top:362px;width:205px;font-size:22px;color:var(--blue)">FIRST RECENTES</h2>

<svg class="intro-frame" viewBox="0 0 86 111" aria-hidden="true">
  <path d="M1 20V1h19" fill="none" stroke="var(--blue)" stroke-width="2"/>
  <path d="M85 92v18H66" fill="none" stroke="#222" stroke-width="2"/>
  <circle cx="37" cy="38" r="12" fill="#333"/>
  <path d="M10 88V64c0-7 6-12 13-12h28c7 0 13 5 13 12v24z" fill="#333"/>
  <path d="M31 52l6 22 6-22z" fill="#fff"/>
  <path d="M35 55h4l-2 18z" fill="#333"/>
  <rect x="45" y="70" width="11" height="2" fill="#fff"/>
</svg>
<h3 class="intro-heading">FIRST ADDRESS</h3>
<p class="intro-text">Colbey is NOT directly affiliated with the Tellvox project. He is an independent support consultant for Tellvox (and voice services in general to some degree). More importantly he is a great person and quite possibly greatest consultant there is out there, anywhere.Colbey is NOT directly affiliated with the Tellvox project. He is an independent support consultant for Tellvox (and voice services in general to some degree). More importantly he is a great person and quite possibly greatest consultant there is out there, anywhere..</p>
<a class="read-more" href="#">READ MORE</a>

<div class="rule" style="left:41px;top:568px;width:617px"></div>

<h3 class="col-title" style="left:56px;top:589px">SOCIAL MEDIA</h3>
<div class="social-bar">
  <div class="social-mail">
    <svg width="16" height="12" viewBox="0 0 16 12" aria-hidden="true"><rect x=".5" y=".5" width="15" height="11" fill="#fff" stroke="#ddd"/><path d="M1 1l7 6 7-6" fill="none" stroke="#999"/></svg>
  </div>
  <div class="social-links">
    <svg width="16" height="14" viewBox="0 0 16 14" aria-label="Share"><circle cx="3" cy="7" r="2.5" fill="#222"/><circle cx="13" cy="2.5" r="2.5" fill="#222"/><circle cx="13" cy="11.5" r="2.5" fill="#222"/><path d="M3 7L13 2.5M3 7l10 4.5" stroke="#222" stroke-width="1.4"/></svg>
    <svg width="14" height="14" viewBox="0 0 14 14" aria-label="Contact"><path d="M2 1h4l1 3-2 1.5a8 8 0 0 0 3.5 3.5L10 7l3 1v4c0 1-1 1-1 1A11 11 0 0 1 1 2s0-1 1-1z" fill="#222"/></svg>
    <svg width="14" height="14" viewBox="0 0 14 14" aria-label="News feed"><circle cx="2.5" cy="11.5" r="2" fill="#222"/><path d="M1 6a7 7 0 0 1 7 7M1 1a12 12 0 0 1 12 12" fill="none" stroke="#222" stroke-width="2"/></svg>
  </div>
</div>
<h3 class="col-title" style="left:56px;top:679px">SOCIAL MEDIA</h3>
<p class="col-text" style="left:57px;top:702px">Dummy data is benign information that does not Dummy data is benign informatioN.</p>

<div class="reasons"><b>3</b>REASONS TO CHOOSE US</div>
<div class="reasons-art" role="img" aria-label="Paper-craft illustration of a green island world with sailboat and buildings"></div>
<h3 class="col-title" style="left:287px;top:774px">IN OUR CENTER</h3>
<p class="col-text" style="left:250px;top:793px;width:190px;text-align:center">Dummy data is benign information</p>
<svg class="abs" style="left:319px;top:814px" width="40" height="41" viewBox="0 0 40 41" aria-hidden="true">
  <g fill="none" stroke="var(--blue)" stroke-width="3">
    <circle cx="20" cy="22" r="14"/><path d="M20 13v9h7"/><path d="M3 9a8 8 0 0 1 9-6M37 9a8 8 0 0 0-9-6"/><path d="M9 35l-3 4M31 35l3 4"/>
  </g>
</svg>

<h3 class="col-title" style="left:494px;top:589px">OUR HELP FULL</h3>
<p class="col-text" style="left:495px;top:611px">Dummy data is benign information that does not Dummy data is benign informatioN.</p>
<div class="dotted"></div>
<h3 class="col-title" style="left:495px;top:703px">WE CAN HELP OUT</h3>
<p class="col-text" style="left:494px;top:725px">Dummy data is benign information that does not Dummy data is benign informatioN.</p>

<div class="rule" style="left:37px;top:840px;width:206px"></div>
<div class="rule" style="left:450px;top:840px;width:204px"></div>
<h2 class="section-title" style="left:268px;top:866px;width:138px;font-size:22px;color:var(--ink)">OUR PEOPLE</h2>
<div class="rule" style="left:268px;top:897px;width:138px;background:#999"></div>

<div class="people-tab">
  <svg class="abs" style="left:12px;top:15px" width="12" height="12" aria-hidden="true"><circle cx="6" cy="6" r="5" fill="#fff"/></svg>
</div>
<div class="people-pill"></div>
<div class="people-photo" role="img" aria-label="Portrait of Martin Colbey"></div>
<div class="people-name">Name of man</div>
<p class="people-bio" style="left:199px;top:1022px;width:230px">Dummy data is benign information that does not Dummy data is benign informatioN.</p>
<p class="people-bio" style="left:100px;top:1046px;width:330px">Dummy data is benign information that does not Dummy data is benign informatioN.</p>

<h3 class="col-title" style="left:456px;top:931px">OUR CLIENTS FEEDBACK</h3>
<div class="client" style="top:961px"><div class="client-photo" role="img" aria-label="Client portrait"></div><span class="client-quote">I'd like it so much</span><span class="client-name">John</span></div>
<div class="client" style="top:1014px"><div class="client-photo" role="img" aria-label="Client portrait"></div><span class="client-quote">I'd like it so much</span><span class="client-name">John</span></div>
<div class="client" style="top:1068px"><div class="client-photo" role="img" aria-label="Client portrait"></div><span class="client-quote">I'd like it so much</span><span class="client-name">John</span></div>

<footer class="site-footer">
  <nav class="foot-nav">
    <a href="#" style="left:180px">HOME</a>
    <a href="#" style="left:243px">ABOUT</a>
    <a href="#" style="left:301px">SECTIONS</a>
    <a href="#" style="left:362px">SERVICES</a>
    <a href="#" style="left:428px">CAREERS</a>
    <a href="#" style="left:489px">CONTACT</a>
  </nav>
  <span class="foot-sep" style="left:221px"></span>
  <span class="foot-sep" style="left:284px"></span>
  <span class="foot-sep" style="left:348px"></span>
  <span class="foot-sep" style="left:417px"></span>
  <span class="foot-sep" style="left:475px"></span>
  <svg class="abs" style="left:576px;top:10px" width="9" height="8" viewBox="0 0 9 8" aria-hidden="true"><path d="M1 4L4.5 1 8 4v4H1z" fill="none" stroke="#fff"/></svg>
  <svg class="abs" style="left:593px;top:9px" width="10" height="10" viewBox="0 0 10 10" aria-hidden="true"><circle cx="4" cy="4" r="3" fill="none" stroke="#fff"/><path d="M6 6l3 3" stroke="#fff" stroke-width="1.4"/></svg>
  <div class="copyright">ALL RIGHTS RESERVED</div>
</footer>

</body>
</html>
```